Bref créative
plumbing
KORLITH PLUMBING INC
Use same font as used in my logo
MARTIN OKAFOR
SERVICE MANAGER
3815 QUILLEN RIDGE DR LAS VEGAS NEVADA 89104
MOKAFOR@KORLITHPLUMBINGINC.EXAMPLE
WWW.KORLITHPLUMBINGINC.EXAMPLE
NV CL #41826
PLEASE USE COMPANY LOGO

```html
<!DOCTYPE html>
<html lang="en">
<head>
<meta charset="utf-8">
<title>Korlith Plumbing Inc — Stationery</title>
<link href="https://fonts.googleapis.com/css2?family=Montserrat:wght@600;800&family=Open+Sans:wght@400;600;700&display=swap" rel="stylesheet">
<style>
  :root {
    --bg: #262626;
    --paper: #ffffff;
    --ink: #1d2a36;
    --blue: #2a9fd8;
    --grey: #8a8f94;
    --rule: #c9cdd1;
    --window: #e4e6e8;
  }
  * { box-sizing: border-box; margin: 0; padding: 0; }
  html, body { width: 1200px; height: 754px; overflow: hidden; background: var(--bg); }
  body { position: relative; font-family: "Open Sans", Arial, sans-serif; color: var(--ink); }

  .sheet { position: absolute; background: var(--paper); }
  .brand { display: flex; align-items: center; gap: 6px; }
  .brand-dot { width: 12px; height: 12px; border-radius: 50%; background: var(--blue); flex: none; }
  .brand-name { font-family: "Montserrat", Arial, sans-serif; font-weight: 800; color: var(--ink); font-size: 11px; letter-spacing: .5px; line-height: 1.1; }

  .phone { font-family: "Montserrat", Arial, sans-serif; font-weight: 800; color: var(--ink); }
  .strip { color: var(--blue); font-weight: 700; font-size: 6.5px; letter-spacing: .3px; text-transform: uppercase; line-height: 1.6; }

  /* Page footer: rule above, address lines below */
  .page-footer { position: absolute; left: 22px; right: 22px; bottom: 18px; border-top: 1px solid var(--blue); padding-top: 6px; }
  .page-footer .strip { text-align: center; }

  /* Letterhead */
  .letterhead { left: 40px; top: 40px; width: 300px; height: 424px; padding: 22px; }
  .letterhead .phone { position: absolute; right: 22px; top: 26px; font-size: 12px; }

  /* Fax sheet */
  .fax { left: 370px; top: 40px; width: 300px; height: 424px; padding: 22px; }
  .fax .phone { position: absolute; right: 22px; top: 26px; font-size: 12px; }
  .fax-title { position: absolute; right: 22px; top: 120px; font-family: "Montserrat", Arial, sans-serif; font-weight: 800; font-size: 14px; }
  .fax-table { position: absolute; left: 22px; top: 62px; width: 170px; border-collapse: collapse; font-size: 6.5px; font-weight: 600; }
  .fax-table td { border: 1px solid var(--rule); padding: 4px 5px; height: 16px; }
  .fax-table td:first-child { width: 44px; color: var(--grey); }

  /* Envelopes */
  .envelope { width: 460px; height: 210px; padding: 20px; }
  .env-plain { left: 710px; top: 40px; }
  .env-window { left: 710px; top: 280px; }
  .env-return { margin-top: 6px; font-size: 6.5px; color: var(--grey); line-height: 1.5; }
  .env-window .window { position: absolute; right: 30px; bottom: 40px; width: 200px; height: 70px; background: var(--window); }
  .envelope .strip { position: absolute; left: 20px; right: 20px; bottom: 14px; }

  /* Business cards */
  .card { top: 520px; width: 320px; height: 182px; padding: 18px; }
  .card-front { left: 40px; }
  .card-back { left: 390px; }
  .card-front .phone { font-size: 26px; margin-top: 28px; }
  .card-front .strip { margin-top: 8px; font-size: 7px; }
  .card-back .brand { justify-content: flex-end; }
  .person { margin-top: 34px; }
  .person-name { font-family: "Montserrat", Arial, sans-serif; font-weight: 800; font-size: 15px; }
  .person-role { font-size: 8px; font-weight: 700; color: var(--blue); letter-spacing: 1px; margin-top: 2px; }
  .contact { margin-top: 14px; font-size: 7.5px; font-weight: 600; line-height: 1.7; }
  .contact svg { width: 8px; height: 8px; vertical-align: -1px; margin-right: 4px; fill: var(--blue); }
  .card-back .bar { position: absolute; left: 0; bottom: 0; width: 100%; height: 6px; background: var(--blue); }
</style>
</head>
<body>

  <section class="sheet letterhead">
    <div class="brand"><span class="brand-dot"></span><span class="brand-name">KORLITH<br>PLUMBING INC</span></div>
    <div class="phone">702-555-0148</div>
    <div class="page-footer">
      <div class="strip">3815 Quillen Ridge Dr Las Vegas Nevada 89104<br>www.korlithplumbinginc.example &nbsp;|&nbsp; NV CL #41826</div>
    </div>
  </section>

  <section class="sheet fax">
    <div class="brand"><span class="brand-dot"></span><span class="brand-name">KORLITH<br>PLUMBING INC</span></div>
    <div class="phone">702-555-0148</div>
    <table class="fax-table">
      <tr><td>TO</td><td></td></tr>
      <tr><td>FROM</td><td></td></tr>
      <tr><td>FAX</td><td></td></tr>
      <tr><td>PHONE</td><td></td></tr>
      <tr><td>DATE</td><td></td></tr>
      <tr><td>PAGES</td><td></td></tr>
    </table>
    <div class="fax-title">FAX</div>
    <div class="page-footer">
      <div class="strip">3815 Quillen Ridge Dr Las Vegas Nevada 89104<br>www.korlithplumbinginc.example &nbsp;|&nbsp; NV CL #41826</div>
    </div>
  </section>

  <section class="sheet envelope env-plain">
    <div class="brand"><span class="brand-dot"></span><span class="brand-name">KORLITH<br>PLUMBING INC</span></div>
    <div class="env-return">3815 Quillen Ridge Dr<br>Las Vegas Nevada 89104</div>
    <div class="strip">3815 Quillen Ridge Dr Las Vegas Nevada 89104 &nbsp;|&nbsp; 702-555-0148 &nbsp;|&nbsp; NV CL #41826</div>
  </section>

  <section class="sheet envelope env-window">
    <div class="brand"><span class="brand-dot"></span><span class="brand-name">KORLITH<br>PLUMBING INC</span></div>
    <div class="env-return">3815 Quillen Ridge Dr<br>Las Vegas Nevada 89104</div>
    <div class="window"></div>
    <div class="strip">3815 Quillen Ridge Dr Las Vegas Nevada 89104 &nbsp;|&nbsp; 702-555-0148 &nbsp;|&nbsp; NV CL #41826</div>
  </section>

  <section class="sheet card card-front">
    <div class="brand"><span class="brand-dot"></span><span class="brand-name">KORLITH<br>PLUMBING INC</span></div>
    <div class="phone">702-555-0148</div>
    <div class="strip">3815 Quillen Ridge Dr<br>Las Vegas Nevada 89104 &nbsp;·&nbsp; NV CL #41826</div>
  </section>

  <section class="sheet card card-back">
    <div class="brand"><span class="brand-dot"></span><span class="brand-name">KORLITH PLUMBING INC</span></div>
    <div class="person">
      <div class="person-name">MARTIN OKAFOR</div>
      <div class="person-role">SERVICE MANAGER</div>
    </div>
    <div class="contact">
      <div><svg viewBox="0 0 10 10"><path d="M1 0h3v3L2.5 4a6 6 0 0 0 3.5 3.5L7 6h3v3c0 .6-.4 1-1 1A9 9 0 0 1 0 1c0-.6.4-1 1-1z"/></svg>702-555-0148</div>
      <div><svg viewBox="0 0 10 10"><path d="M0 2h10v6H0z M0 2l5 3.5L10 2" fill="none" stroke="#2a9fd8" stroke-width="1.2"/></svg>MOKAFOR@KORLITHPLUMBINGINC.EXAMPLE</div>
      <div><svg viewBox="0 0 10 10"><circle cx="5" cy="5" r="4" fill="none" stroke="#2a9fd8" stroke-width="1.2"/></svg>WWW.KORLITHPLUMBINGINC.EXAMPLE</div>
    </div>
    <div class="bar"></div>
  </section>

</body>
</html>
```